STATIONERY FOR OUR CLIENT

I have a client that is a major oilseed processor in Australia. They want a deluxe gorgeous version of their business card.
I am proposing we print the business cards in Pressly.com KALVO versions with the coloured edging, probably in black. Their business name needs to appear on both sides whether in logo or text.
The stationery needs to be layed up to look lifelike to impress the client. Ideally full stationery including letterhead, business card, with compliments, envelopes.
We want to impress our client.
*** The design needs to communicate - quality, premium, prestige, modern, expert, wealthy, abundant, sophisticated, established.
Designs need to be not too dark, not alot of black please. Clean, modern, sophisticated, upmarket, luxury brand.
I need 3 concepts to present to client and once approved, refined to then have print ready files - and working files just in case we have to make tweaks down the track.
We also need to create a one page style guide, that includes pms colour etc.
THIS IS AN URGENT JOB
Updates

Please design less with black more with clean white possibly light grey/beige as secondary colour if you are looking for contrast. I have added some examples of cards that look nice and might help with what the client is looking for. thank you and looking forward to seeing the designs

Please ensure all designs submitted have the correct contact details of our client which is in the brief. Also please do not have any black backgrounds - if any of your design do have black backgrounds, please amend. Thank you

Target Market(s)

business customers, investors, major distributors

Industry/Entity Type

Business

Font styles to use
Sans Serif

Requirements
Must have
• must have business name on both sides. designed to be printed with pressly.com using their KALVO business card print offering.
Should not have
• alot of black

```html
<!DOCTYPE html>
<html lang="en">
<head>
<meta charset="utf-8">
<title>Orva business cards</title>
<link href="https://fonts.googleapis.com/css2?family=Open+Sans:wght@400;700&display=swap" rel="stylesheet">
<style>
  :root {
    --backdrop: #07894d;
    --brand-green: #0c8a47;
    --paper: #ffffff;
    --edge: #231f20;
    --ink: #231f20;
  }
  * { box-sizing: border-box; margin: 0; padding: 0; }
  html, body { width: 1200px; height: 821px; overflow: hidden; }
  body {
    background: var(--backdrop);
    font-family: "Open Sans", Arial, sans-serif;
    position: relative;
  }
  .card {
    position: absolute;
    width: 636px;
    height: 362px;
    border-radius: 40px;
    overflow: hidden;
  }
  /* Front face */
  .card-front {
    left: 47px; top: 420px;
    background: var(--paper);
  }
  .front-mark {
    position: absolute;
    left: 268px; top: 48px;
    width: 100px; height: 100px;
    border-radius: 50%;
    background: var(--brand-green);
  }
  .front-name {
    position: absolute;
    left: 0; right: 0; top: 162px;
    text-align: center;
    color: var(--brand-green);
    font-size: 52px;
    font-weight: 400;
    letter-spacing: 0.55em;
    text-indent: 0.55em;
    line-height: 1;
  }
  .front-tagline {
    position: absolute;
    left: 0; right: 0; top: 228px;
    text-align: center;
    color: var(--brand-green);
    font-size: 25px;
    line-height: 1;
  }
  .front-footer {
    position: absolute;
    left: 8px; right: 8px; top: 300px;
    display: flex; align-items: center; gap: 56px;
  }
  .front-footer .rule {
    flex: 1;
    height: 4px;
    background: var(--brand-green);
  }
  .front-footer .web {
    color: var(--brand-green);
    font-size: 15px;
    font-weight: 700;
    letter-spacing: 0.28em;
  }
  /* Back face */
  .card-back {
    left: 530px; top: 36px;
    background: var(--edge);
    padding: 12px;
  }
  .back-inner {
    position: relative;
    width: 100%;
    height: 306px;
    background: var(--paper);
    border-radius: 30px 30px 6px 6px;
  }
  .back-mark {
    position: absolute;
    left: 22px; top: 26px;
    width: 56px; height: 56px;
    border-radius: 50%;
    background: var(--brand-green);
  }
  .back-name {
    position: absolute;
    left: 150px; top: 28px;
    color: var(--brand-green);
    font-size: 58px;
    letter-spacing: 0.62em;
    line-height: 1;
  }
  .back-tagline {
    position: absolute;
    left: 150px; top: 96px;
    color: var(--brand-green);
    font-size: 27px;
    line-height: 1;
  }
  .person {
    position: absolute;
    left: 28px; top: 150px;
  }
  .person-name {
    color: var(--brand-green);
    font-size: 27px;
    font-weight: 700;
    line-height: 1.1;
  }
  .person-role {
    color: var(--ink);
    font-size: 19px;
    line-height: 1.2;
  }
  .address {
    position: absolute;
    left: 300px; top: 150px;
    color: var(--ink);
    font-size: 15px;
    font-weight: 700;
    line-height: 1.3;
  }
  .contacts {
    position: absolute;
    left: 272px; top: 196px;
    list-style: none;
  }
  .contacts li {
    display: flex; align-items: center; gap: 12px;
    color: var(--ink);
    font-size: 15px;
    font-weight: 700;
    line-height: 21px;
  }
  .contacts svg { width: 14px; height: 14px; flex: none; }
  .back-footer {
    position: absolute;
    left: 0; right: 0; bottom: 0;
    height: 44px;
    display: flex; align-items: center; justify-content: center;
    color: var(--paper);
    font-size: 16px;
    font-weight: 700;
    letter-spacing: 0.3em;
  }
</style>
</head>
<body>

<section class="card card-back" aria-label="Business card, back">
  <div class="back-inner">
    <span class="back-mark" aria-hidden="true"></span>
    <div class="back-name">ORVA</div>
    <div class="back-tagline">Orvale Seeds &amp; BioPower</div>

    <div class="person">
      <div class="person-name">M.K. Halden</div>
      <div class="person-role">Managing Director</div>
    </div>

    <div class="address">Unit 7, 48 Ferngrove Road<br>Ashvale VIC 3199</div>

    <ul class="contacts">
      <li>
        <svg viewBox="0 0 14 14" aria-hidden="true"><path d="M3 1h2l1 3-1.5 1a7 7 0 0 0 4.5 4.5L10 8l3 1v2a2 2 0 0 1-2 2A10 10 0 0 1 1 3a2 2 0 0 1 2-2z" fill="var(--brand-green)"/></svg>
        03 9000 1234
      </li>
      <li>
        <svg viewBox="0 0 14 14" aria-hidden="true"><rect x="3.5" y="1" width="7" height="12" rx="1.2" fill="none" stroke="var(--brand-green)" stroke-width="1.6"/></svg>
        0400 000 111
      </li>
      <li>
        <svg viewBox="0 0 14 14" aria-hidden="true"><rect x="1" y="3" width="12" height="8" fill="none" stroke="var(--brand-green)" stroke-width="1.4"/><path d="M1 3l6 5 6-5" fill="none" stroke="var(--brand-green)" stroke-width="1.4"/></svg>
        hello@orvaleseeds.com
      </li>
      <li>
        <svg viewBox="0 0 14 14" aria-hidden="true"><rect x="1" y="1" width="12" height="12" fill="var(--brand-green)"/></svg>
        orvaleseeds.com/social
      </li>
    </ul>
  </div>
  <div class="back-footer">orvaleseeds.com.au</div>
</section>

<section class="card card-front" aria-label="Business card, front">
  <span class="front-mark" aria-hidden="true"></span>
  <div class="front-name">ORVA</div>
  <div class="front-tagline">Orvale Seeds &amp; BioPower</div>
  <div class="front-footer">
    <span class="rule"></span>
    <span class="web">orvaleseeds.com.au</span>
    <span class="rule"></span>
  </div>
</section>

</body>
</html>
```